Book Cover Design for a non-fiction novel

For this job, we need creativity and not just a stock photo on a cover.
We are working with 2 titles and subtitles which the cover will help us choose the best one to go with.

No 1
The book title is Across the Quiet River
The subtitle is - Why a Restless Boy Found Deep Patience
Authors name is Tayo Ikeme

No 2
The book title - Vantage
The subtitle - The Tale of a Restless Boy's Passage Through Winter

Let us see your creative side with this job.

Requirements
Must have
• images
Nice to have
• colours

```html
<!DOCTYPE html>
<html lang="en">
<head>
<meta charset="utf-8">
<title>Vantage — Tayo Ikeme</title>
<link href="https://fonts.googleapis.com/css2?family=Big+Shoulders+Display:wght@900&family=Oswald:wght@600;700&display=swap" rel="stylesheet">
<style>
  :root {
    --page: #ffffff;
    --paper: #e9e8e5;
    --paper-dark: #d6d4d0;
    --ink: #0d0d0d;
    --accent-red: #c0121f;
    --sun-core: #ffd21a;
    --sun-mid: #f7931e;
    --sun-edge: #e4471b;
  }
  * { margin: 0; padding: 0; box-sizing: border-box; }
  html, body {
    width: 1036px;
    height: 1200px;
    overflow: hidden;
    background: var(--page);
  }
  .cover {
    position: absolute;
    left: 178px;
    top: 40px;
    width: 680px;
    height: 1120px;
    overflow: hidden;
    background:
      radial-gradient(circle at 30% 20%, rgba(255,255,255,0.6), transparent 60%),
      linear-gradient(160deg, var(--paper), var(--paper-dark));
  }
  .cover-title {
    position: absolute;
    top: 60px;
    left: 0;
    width: 100%;
    text-align: center;
    font-family: "Big Shoulders Display", "Impact", sans-serif;
    font-weight: 900;
    font-size: 200px;
    line-height: 1;
    letter-spacing: 2px;
    color: var(--ink);
    text-transform: uppercase;
    transform: scaleY(1.2);
    transform-origin: top center;
  }
  .cover-subtitle {
    position: absolute;
    top: 335px;
    left: 40px;
    z-index: 2;
    font-family: "Oswald", "Arial Narrow", sans-serif;
    font-weight: 700;
    font-size: 36px;
    line-height: 1.2;
    color: var(--ink);
    text-transform: uppercase;
  }
  .cover-subtitle .highlight { color: var(--accent-red); }
  .cover-art {
    position: absolute;
    left: 0;
    top: 520px;
    width: 100%;
    height: 600px;
    background:
      radial-gradient(circle at 55% 28%, var(--sun-core) 0, var(--sun-mid) 90px, var(--sun-edge) 160px, transparent 175px),
      linear-gradient(180deg, transparent 0, transparent 42%, var(--ink) 48%, var(--ink) 100%);
  }
  .cover-author {
    position: absolute;
    left: 0;
    bottom: 70px;
    width: 100%;
    z-index: 2;
    text-align: center;
    font-family: "Oswald", "Arial Narrow", sans-serif;
    font-weight: 600;
    font-size: 84px;
    line-height: 1;
    color: var(--paper);
    text-transform: uppercase;
  }
</style>
</head>
<body>
  <main class="cover">
    <h1 class="cover-title">Vantage</h1>
    <p class="cover-subtitle">
      The Tale of a<br>
      Restless Boy's<br>
      Passage Through<br>
      <span class="highlight">Winter</span>
    </p>
    <div class="cover-art" role="img" aria-label="Illustration: a setting orange sun with birds behind two black cliff edges split by a gap, one silhouetted figure sitting hunched on the left cliff and a caped figure leaping joyfully on the right"></div>
    <p class="cover-author">Tayo<br>Ikeme</p>
  </main>
</body>
</html>
```